Www.zubwave.com monthly sweepstakes.

Every month I am giving away 1st place $500 gift card to your local RC hobby shop of choice, 2nd place $100 gift card 3rd place ZubWave merch. All things rc: cars, boats, quadcopters, helicopters, airplanes.

Needs to be with the color theme of the website. Check zubwave.com for current sweepstakes banner. New banner should be half the size in height. I will post dimension later.

Target Market(s)

Rc hobbies cars airplanes helicopters boats

Industry/Entity Type

RemoteControl hobbies

Requirements
Must have
• 1440x680 size, Blend with black background, creative and in incorporate all trypes of rc craft
Should not have
• To many different colors, dosnt need logo as its already on website. This is a banner for my homepage

```html
<!DOCTYPE html>
<html lang="en">
<head>
<meta charset="utf-8">
<title>ZubWave Prize Giveaway Banner</title>
<link href="https://fonts.googleapis.com/css2?family=Anton&family=Oswald:wght@600&family=Poppins:wght@500&display=swap" rel="stylesheet">
<style>
  :root {
    --ink: #050505;
    --deep-red: #5a0410;
    --blood: #7a0614;
    --accent: #d8001e;
    --white: #ffffff;
  }
  * { margin: 0; padding: 0; box-sizing: border-box; }
  html, body { width: 1200px; height: 665px; overflow: hidden; background: var(--ink); }
  .banner {
    position: absolute; left: 0; top: 50px; width: 1200px; height: 566px; overflow: hidden;
    background:
      radial-gradient(ellipse 520px 200px at 640px 380px, rgba(0,0,0,0.95), transparent 75%),
      radial-gradient(ellipse 260px 180px at 120px 80px, var(--blood), transparent 80%),
      radial-gradient(ellipse 300px 170px at 1000px 60px, var(--blood), transparent 80%),
      radial-gradient(ellipse 260px 200px at 1140px 300px, var(--deep-red), transparent 80%),
      radial-gradient(ellipse 260px 200px at 60px 460px, var(--deep-red), transparent 80%),
      linear-gradient(180deg, var(--deep-red) 0%, #1a0105 55%, var(--ink) 80%);
  }
  .craft { position: absolute; }
  .craft-jet { left: 0; top: 169px; width: 354px; height: 148px; }
  .craft-drone { left: 716px; top: 62px; width: 403px; height: 164px; }
  .craft-truck { left: 960px; top: 385px; width: 240px; height: 181px; }

  .title { position: absolute; font-family: "Anton", sans-serif; line-height: 1; text-transform: uppercase; transform-origin: left top; white-space: nowrap; }
  .title-prize { left: 434px; top: 60px; font-size: 112px; color: var(--white); letter-spacing: 1px; transform: scaleX(1.06); }
  .title-giveaway { left: 343px; top: 156px; font-size: 108px; color: var(--accent); letter-spacing: 1px; transform: scaleX(1.27); }

  .tag {
    position: absolute; background: var(--accent); color: var(--white); border-radius: 6px;
    font-family: "Oswald", sans-serif; font-size: 19px; line-height: 1; padding: 8px 6px;
    transform: rotate(-6deg); white-space: nowrap; z-index: 2;
  }
  .tag sup { font-size: 9px; }
  .tag-first { left: 410px; top: 284px; }
  .tag-second { left: 217px; top: 382px; }
  .tag-third { left: 918px; top: 326px; }

  .amount { position: absolute; font-family: "Oswald", sans-serif; color: var(--white); line-height: 1; transform-origin: left top; white-space: nowrap; }
  .amount-first { left: 472px; top: 284px; font-size: 108px; letter-spacing: -2px; transform: scaleX(0.64); }
  .amount-second { left: 280px; top: 335px; font-size: 84px; letter-spacing: -2px; transform: scaleX(0.6); }
  .amount-third { left: 807px; top: 338px; font-size: 80px; letter-spacing: -2px; transform: scaleX(0.54); }

  .label { position: absolute; font-family: "Poppins", sans-serif; color: var(--white); line-height: 1; white-space: nowrap; }
  .label-first { left: 609px; top: 300px; font-size: 46px; line-height: 42px; }
  .label-second { left: 266px; top: 414px; font-size: 26px; }
  .label-third { left: 835px; top: 414px; font-size: 26px; }
  .note { position: absolute; left: 470px; top: 405px; width: 260px; text-align: center;
    font-family: "Poppins", sans-serif; font-size: 21px; line-height: 27px; color: var(--white); }

  .divider { position: absolute; top: 344px; width: 2px; height: 124px;
    background: linear-gradient(180deg, transparent, var(--accent) 30%, var(--accent) 70%, transparent); }
  .divider-left { left: 427px; }
  .divider-right { left: 770px; }
</style>
</head>
<body>
  <section class="banner">
    <svg class="craft craft-jet" role="img" aria-label="Red and white RC jet airplane in flight" viewBox="0 0 354 148">
      <defs><linearGradient id="jetTone" x1="0" x2="1"><stop offset="0" stop-color="#b3121f"/><stop offset="0.6" stop-color="#cf2a2f"/><stop offset="1" stop-color="#d9d4cf"/></linearGradient></defs>
      <rect width="354" height="148" rx="60" fill="url(#jetTone)" opacity="0.55"/>
    </svg>
    <svg class="craft craft-drone" role="img" aria-label="Red and black FPV racing quadcopter" viewBox="0 0 403 164">
      <defs><linearGradient id="droneTone" x1="0" x2="1"><stop offset="0" stop-color="#c61a26"/><stop offset="0.5" stop-color="#2a2a2a"/><stop offset="1" stop-color="#c61a26"/></linearGradient></defs>
      <rect width="403" height="164" rx="50" fill="url(#droneTone)" opacity="0.55"/>
    </svg>
    <svg class="craft craft-truck" role="img" aria-label="Bronze RC off-road truck kicking up orange dust" viewBox="0 0 240 181">
      <defs><linearGradient id="truckTone" x1="0" y1="0" x2="0" y2="1"><stop offset="0" stop-color="#8a5a2c"/><stop offset="0.7" stop-color="#3a2a1c"/><stop offset="1" stop-color="#c2410c"/></linearGradient></defs>
      <rect width="240" height="181" rx="40" fill="url(#truckTone)" opacity="0.6"/>
    </svg>

    <h1>
      <span class="title title-prize">Prize</span>
      <span class="title title-giveaway">Giveaway</span>
    </h1>

    <div class="divider divider-left"></div>
    <div class="divider divider-right"></div>

    <div class="prize prize-second">
      <span class="amount amount-second">$100</span>
      <span class="label label-second">Gift Card</span>
      <span class="tag tag-second">2<sup>nd</sup> Prize</span>
    </div>

    <div class="prize prize-first">
      <span class="amount amount-first">$500</span>
      <span class="label label-first">Gift<br>Card</span>
      <p class="note">to your local RC hobby shop of choice</p>
      <span class="tag tag-first">1<sup>st</sup> Prize</span>
    </div>

    <div class="prize prize-third">
      <span class="amount amount-third">ZubWave</span>
      <span class="label label-third">Merch</span>
      <span class="tag tag-third">3<sup>rd</sup> Prize</span>
    </div>
  </section>
</body>
</html>
```